Poster around the theme Haverlinger’s cat - Brindlewood Computing

We need a poster so we can have it framed to be displayed on our office wall. Poster should be around the theme Haverlinger’s cat. A little bit about our company - Brindlewood Computing is a Deep-Tech company developing Quantum Software for Extreme Ideas. See attached some reference images.

```html
<!DOCTYPE html>
<html lang="en">
<head>
<meta charset="utf-8">
<title>Wanted: Haverlinger's Cat — Brindlewood Computing</title>
<link rel="stylesheet" href="https://fonts.googleapis.com/css2?family=Alfa+Slab+One&family=Exo+2:wght@400;600&display=swap">
<style>
  :root {
    --backdrop: #f3f2f3;
    --frame: #0b0b0b;
    --paper-light: #e6c39a;
    --paper-mid: #d6a466;
    --paper-warm: #c98d4c;
    --ink: #1e1b18;
    --rust: #8b3a10;
    --brand: #ffffff;
    --portrait-deep: #b5520f;
    --portrait-bright: #e07f1e;
  }
  * { margin: 0; padding: 0; box-sizing: border-box; }
  html, body {
    width: 1200px; height: 1200px; overflow: hidden;
    background: var(--backdrop);
  }
  .poster {
    position: absolute; left: 261px; top: 99px;
    width: 678px; height: 1018px;
    background: var(--frame);
  }
  .paper {
    position: absolute; left: 40px; top: 25px;
    width: 601px; height: 957px;
    background:
      radial-gradient(ellipse at 30% 25%, rgba(230,170,80,.55), transparent 60%),
      radial-gradient(ellipse at 75% 80%, rgba(240,200,165,.6), transparent 55%),
      linear-gradient(170deg, var(--paper-mid), var(--paper-light) 55%, var(--paper-warm));
    clip-path: polygon(0 0, 28% 0.4%, 44% 0.2%, 58% 1.6%, 62% 0, 100% 0, 99.4% 6%, 100% 18%, 99% 32%, 100% 44%, 98.6% 58%, 100% 60%, 99.2% 76%, 100% 90%, 99.5% 100%, 70% 99.6%, 40% 100%, 12% 99.5%, 0 100%, 0.8% 86%, 0 74%, 2.4% 72%, 0.6% 62%, 2% 48%, 0 40%, 1.6% 30%, 0 18%, 0.6% 8%);
  }
  .typeset {
    position: absolute; inset: 0; width: 601px; height: 957px;
  }
  .brand-name, .brand-sub {
    fill: var(--brand); font-family: "Exo 2", sans-serif; font-weight: 600;
  }
  .brand-sub { font-weight: 400; }
  .slab { font-family: "Alfa Slab One", serif; fill: var(--ink); }
  .amp { fill: var(--rust); }
  .rule {
    position: absolute; top: 314px; left: 67px; width: 481px; height: 2px;
    background: var(--ink);
  }
  .portrait {
    position: absolute; top: 334px; left: 147px; width: 307px; height: 405px;
    background: radial-gradient(ellipse at 50% 55%, var(--portrait-bright), var(--portrait-deep));
    border: 2px solid #3a2210;
  }
</style>
</head>
<body>
  <div class="poster">
    <div class="paper">
      <div class="rule"></div>
      <div class="portrait" role="img" aria-label="Illustration of a grey cat in round glasses peeking out of an orange box, holding a red quantum mechanics book"></div>
      <svg class="typeset" viewBox="0 0 601 957">
        <defs>
          <polygon id="star" points="15,2 18.5,11 28,11 20.5,17 23.5,27 15,21 6.5,27 9.5,17 2,11 11.5,11"/>
        </defs>
        <text class="brand-name" x="300" y="67" text-anchor="middle" font-size="39" textLength="314" lengthAdjust="spacingAndGlyphs">BRINDLEWOOD</text>
        <text class="brand-sub" x="300" y="98" text-anchor="middle" font-size="21" textLength="118" lengthAdjust="spacingAndGlyphs">COMPUTING</text>
        <text class="slab" x="300" y="242" text-anchor="middle" font-size="180" textLength="509" lengthAdjust="spacingAndGlyphs">WANTED</text>
        <text class="slab" x="300" y="298" text-anchor="middle" font-size="44" textLength="346" lengthAdjust="spacingAndGlyphs">DEAD <tspan class="amp">&amp;</tspan> ALIVE</text>
        <text class="slab" x="300" y="801" text-anchor="middle" font-size="56" textLength="473" lengthAdjust="spacingAndGlyphs"><tspan font-size="75">H</tspan>AVERLINGER’s</text>
        <text class="slab" x="300" y="870" text-anchor="middle" font-size="76" textLength="173" lengthAdjust="spacingAndGlyphs">CAT</text>
        <g fill="#1e1b18">
          <use href="#star" x="87" y="827"/><use href="#star" x="124" y="827"/><use href="#star" x="161" y="827"/>
          <use href="#star" x="410" y="827"/><use href="#star" x="452" y="827"/><use href="#star" x="493" y="827"/>
        </g>
      </svg>
    </div>
  </div>
</body>
</html>
```